Eco friendly Swedish beauty products sold in aluminum bottles - label design needed

We need help in designing a series of stick on labels for 80 ml (2.7 fl. oz.) aluminum bottles containing beauty products such as soaps, shampoo etc. The diameter of the bottle is 36 mm and the body of the bottles measures approx. 106 mm.
It is important for us that the label has a simplistic and clean feel with few colors (and the right ones!) and that the label helps amplify this product being both better and a more sustainable alternative to many of our plastic bottle competitors. The design and label should communicate the feel of an Eco-friendly, sustainable and modern brand of high quality - and with a Swedish concept.
We are using Montserrat font in our materials. Find attached information of preferred colors, the bottles and one example of our logotype. I am also available on e-mail should further information be needed.

Looking forward and very excited to receive your suggestions.
Note that we are expecting to start selling a series of approximately 10 different products where I will need one "master design" and then only smaller changes for each of the different products.

Target Market(s)

People whom are aware and not only look at price tag. Private and commercial market.

Industry/Entity Type

Beauty

Font styles to use
Other font styles liked:
• Montserrat

Requirements
Must have
• It must give the feel of being both better and a more sustainable alternative to many of our plastic bottle competitors.
Nice to have
• Simplistic. Clean. Clear.
Should not have
• Wrong colors, too complex designs.

```html
<!DOCTYPE html>
<html lang="en">
<head>
<meta charset="utf-8">
<title>Pure by Lundén – Hair shampoo label</title>
<link href="https://fonts.googleapis.com/css2?family=Montserrat:wght@300;400;600&display=swap" rel="stylesheet">
<style>
  :root {
    --paper: #ffffff;
    --copper: #a8641a;
    --cream: #f4efe6;
    --sage: #7b806a;
    --ink: #1f1f1a;
    --mist: #eceee4;
    --peach: #d9a27a;
    --metal-dark: #7c7c7a;
    --metal-light: #c9c9c6;
  }
  * { margin: 0; padding: 0; box-sizing: border-box; }
  html, body {
    width: 1200px; height: 1008px; overflow: hidden;
    background: var(--paper);
    font-family: "Montserrat", sans-serif;
  }
  .board { position: relative; width: 1200px; height: 1008px; }
  .board-frame {
    position: absolute; left: 16px; top: 22px; width: 1170px; height: 972px;
    border: 1px solid var(--copper); border-radius: 3px;
  }
  .brand-name {
    position: absolute; right: 51px; top: 82px;
    font-size: 72px; font-weight: 400; letter-spacing: 2px;
    color: var(--copper); white-space: nowrap; line-height: 1;
  }
  .bottle-photo {
    position: absolute; left: 199px; top: 137px; width: 215px; height: 770px;
    border-radius: 60px 60px 24px 24px;
    background: linear-gradient(90deg, var(--metal-dark), var(--metal-light) 45%, var(--metal-dark));
  }
  .label {
    position: absolute; left: 129px; top: 490px; width: 642px; height: 321px;
    background: var(--cream);
  }
  .label-top {
    position: absolute; left: 8px; top: 10px; width: 627px; height: 151px;
    background: var(--sage);
  }
  .label-brand {
    position: absolute; left: 14px; top: 38px;
    font-size: 17px; font-weight: 400; letter-spacing: 1px;
    color: var(--ink); white-space: nowrap;
  }
  .label-claim {
    position: absolute; left: 302px; top: 115px;
    transform: rotate(-90deg); transform-origin: left top;
    font-size: 12px; font-weight: 300; letter-spacing: .5px;
    color: var(--mist); white-space: nowrap;
  }
  .label-bottom {
    position: absolute; left: 8px; top: 173px; width: 627px; height: 141px;
    border: 1px solid #333; border-radius: 3px;
  }
  .product-name {
    position: absolute; left: 8px; top: 118px;
    transform: rotate(-90deg); transform-origin: left top;
    font-size: 13px; font-weight: 300; letter-spacing: .5px;
    color: #333; white-space: nowrap;
  }
  .leaf-art {
    position: absolute; left: 294px; top: 43px; width: 39px; height: 70px;
    border-radius: 50% 10% 50% 10%;
    background: #2a2a26;
  }
  .volume {
    position: absolute; left: 517px; top: 119px;
    font-size: 7px; font-weight: 600; color: var(--peach);
  }
</style>
</head>
<body>
  <main class="board">
    <div class="board-frame"></div>
    <h1 class="brand-name">PURE BY LUNDÉN</h1>
    <div class="bottle-photo" role="img" aria-label="Photo of a brushed aluminium bottle with threaded neck"></div>
    <section class="label">
      <div class="label-top">
        <p class="label-brand">PURE BY LUNDÉN</p>
        <p class="label-claim">Eco friendly</p>
      </div>
      <div class="label-bottom">
        <p class="product-name">Hair shampoo</p>
        <div class="leaf-art" role="img" aria-label="Ink brush illustration of a single leaf"></div>
        <p class="volume">ml 80</p>
      </div>
    </section>
  </main>
</body>
</html>
```